Pest Control Company needs business card!

Hi there, we need a business card designed for our new Pest Control Company. Ideally this card will be simple, yet feel elegant and high end. We want to use the colours Orange, Black and White. Please see our attached logo for the exact colours.

Business card details:

Phone - 0461 275 804
Name - Gavin Holloway
Email - Info@steadfastverminguard.com.au

We would also like to include the following list with dot points:

SERVICES / INSPECTIONS

Termites, Wood Borers, Ants, Cockroaches, Spiders, Fleas, Mice, Rats, Bed Bugs, & More!

```html
<!DOCTYPE html>
<html lang="en">
<head>
<meta charset="utf-8">
<title>Steadfast Vermin Guard – Business Card</title>
<link rel="stylesheet" href="https://fonts.googleapis.com/css2?family=Quicksand:wght@500;700&display=swap">
<style>
  :root {
    --orange: #f0861f;
    --orange-deep: #d96d12;
    --black: #141414;
    --white: #ffffff;
    --stage: #5e6062;
    --body-text: #1c1c1c;
  }
  * { box-sizing: border-box; margin: 0; padding: 0; }
  html, body {
    width: 1200px; height: 1000px; overflow: hidden;
    background: var(--stage);
    font-family: "Quicksand", sans-serif;
  }
  .sheet {
    width: 1200px; height: 1000px;
    display: flex; flex-direction: column; align-items: center; justify-content: center;
    gap: 60px;
  }
  .card {
    position: relative;
    width: 700px; height: 400px;
    overflow: hidden;
    box-shadow: 0 10px 28px rgba(0,0,0,.35);
  }

  /* Front – contact side */
  .card--contact { background: var(--white); }
  .card__panel { position: absolute; inset: 0; }
  .contact {
    position: absolute; left: 38px; top: 38px;
    color: var(--body-text);
  }
  .contact__name {
    color: var(--orange);
    font-weight: 700; font-size: 28px; letter-spacing: 1.5px;
    text-transform: uppercase;
    margin-bottom: 22px;
  }
  .contact__line {
    display: flex; align-items: center; gap: 16px;
    font-weight: 500; font-size: 16px;
    margin-bottom: 14px;
  }
  .contact__icon {
    width: 30px; height: 30px; border-radius: 50%;
    background: var(--black);
    display: flex; align-items: center; justify-content: center;
    flex: none;
  }
  .services { margin-top: 28px; }
  .services__title {
    color: var(--orange);
    font-weight: 700; font-size: 17px; letter-spacing: .6px;
    margin-bottom: 12px;
  }
  .services__list {
    list-style: none;
    display: grid; grid-template-columns: 170px 170px; grid-auto-flow: column;
    grid-template-rows: repeat(5, auto);
    row-gap: 6px;
    font-weight: 500; font-size: 15.5px;
  }
  .services__item { display: flex; align-items: center; gap: 10px; }
  .services__item::before {
    content: ""; width: 9px; height: 9px; border-radius: 50%;
    border: 2px solid var(--black);
    background: radial-gradient(circle, var(--black) 0 2px, transparent 2.5px);
    flex: none;
  }

  /* Back – brand side */
  .card--brand {
    background: linear-gradient(135deg, var(--orange) 0%, var(--orange-deep) 100%);
    display: flex; align-items: center; justify-content: center;
  }
  .brand { display: flex; align-items: center; gap: 22px; }
  .brand__dot {
    width: 34px; height: 34px; border-radius: 50%;
    background: var(--black);
  }
  .brand__name {
    color: var(--black);
    font-weight: 700; font-size: 50px; line-height: 1.02;
    text-transform: uppercase; letter-spacing: 1px;
  }
</style>
</head>
<body>
<main class="sheet">

  <section class="card card--contact" aria-label="Business card, contact side">
    <svg class="card__panel" width="700" height="400" viewBox="0 0 700 400" aria-hidden="true">
      <defs>
        <linearGradient id="panelOrange" x1="0" y1="0" x2="1" y2="1">
          <stop offset="0" stop-color="#f0861f"/>
          <stop offset="1" stop-color="#d96d12"/>
        </linearGradient>
      </defs>
      <polygon points="460,0 700,0 700,400 352,400" fill="url(#panelOrange)"/>
      <polygon points="450,0 462,0 354,400 342,400" fill="#141414"/>
    </svg>

    <div class="contact">
      <h1 class="contact__name">Gavin Holloway</h1>
      <p class="contact__line">
        <span class="contact__icon">
          <svg width="16" height="16" viewBox="0 0 24 24" aria-hidden="true"><path fill="#fff" d="M6.6 10.8a15.1 15.1 0 0 0 6.6 6.6l2.2-2.2c.3-.3.7-.4 1-.2 1.1.4 2.3.6 3.6.6.6 0 1 .4 1 1V20c0 .6-.4 1-1 1A17 17 0 0 1 3 4c0-.6.4-1 1-1h3.5c.6 0 1 .4 1 1 0 1.3.2 2.5.6 3.6.1.3 0 .7-.2 1z"/></svg>
        </span>
        0461 275 804
      </p>
      <p class="contact__line">
        <span class="contact__icon">
          <svg width="16" height="16" viewBox="0 0 24 24" aria-hidden="true"><path fill="#fff" d="M3 6h18v12H3z"/><path fill="none" stroke="#141414" stroke-width="1.8" d="M3 6l9 7 9-7"/></svg>
        </span>
        Info@steadfastverminguard.com.au
      </p>

      <div class="services">
        <h2 class="services__title">SERVICES / INSPECTIONS</h2>
        <ul class="services__list">
          <li class="services__item">Termites</li>
          <li class="services__item">Ants</li>
          <li class="services__item">Spiders</li>
          <li class="services__item">Mice</li>
          <li class="services__item">Bed Bugs</li>
          <li class="services__item">Wood Borers</li>
          <li class="services__item">Cockroaches</li>
          <li class="services__item">Fleas</li>
          <li class="services__item">Rats</li>
          <li class="services__item">More!</li>
        </ul>
      </div>
    </div>
  </section>

  <section class="card card--brand" aria-label="Business card, brand side">
    <div class="brand">
      <span class="brand__dot" aria-hidden="true"></span>
      <p class="brand__name">Steadfast<br>Vermin<br>Guard</p>
    </div>
  </section>

</main>
</body>
</html>
```